Construction Directory Website Flyer

We need a postcard size +/- or somewhere around that size (something standard) flyer designed for our construction directory website. Leave a spot for tagline. Call to action is 'register your company now'. I am thinking many mini pictures of different construction to show that it is for the entire construction industry. Logo and screenshot of the homepage of the website is attached. Use same theme as webpage.

Target Market(s)

Construction Industry

Industry/Entity Type

Construction

Font styles to use
Sans Serif

Requirements
Must have
• Call to action
• Colors to match logo
• Area to add description and details.
Nice to have
• Construction Images
Should not have
• No Cartoonish types of things

```html
<!DOCTYPE html>
<html lang="en">
<head>
<meta charset="utf-8">
<title>Buildwise Hub – Register Your Company</title>
<link rel="stylesheet" href="https://fonts.googleapis.com/css2?family=Open+Sans:wght@400;600;700&family=Oswald:wght@700&display=swap">
<style>
  :root {
    --orange: #e0492a;
    --charcoal: #474b54;
    --dark-strip: #3e434c;
    --ink: #1f1f22;
    --paper: #ffffff;
    --header-bg: #ececee;
    --gallery-top: #f4f4f6;
    --gallery-bottom: #dcdde0;
    --frame: #4a4f58;
    --canvas-bg: #eeeeee;
  }
  * { box-sizing: border-box; margin: 0; padding: 0; }
  html, body { width: 1200px; height: 1200px; overflow: hidden; }
  body {
    background: var(--canvas-bg);
    font-family: "Open Sans", Arial, sans-serif;
    position: relative;
  }
  .flyer {
    position: absolute;
    left: 181px; top: 20px;
    width: 837px; height: 1160px;
    background: var(--paper);
    display: flex; flex-direction: column;
    box-shadow: 0 6px 18px rgba(0,0,0,.18);
  }
  .top-strip { height: 9px; background: var(--dark-strip); }
  .masthead {
    height: 131px;
    background: linear-gradient(#f6f6f7, var(--header-bg));
    display: flex; align-items: center;
    position: relative;
  }
  .brand {
    width: 385px; height: 100%;
    display: flex; align-items: center; gap: 12px;
    padding-left: 48px;
    border-right: 2px solid #d4d5d8;
  }
  .brand-mark { width: 30px; height: 30px; background: var(--orange); flex: none; }
  .brand-name {
    font-weight: 600; font-size: 31px; color: var(--charcoal);
    line-height: 1; letter-spacing: .5px;
  }
  .tagline {
    padding-left: 28px;
    font-weight: 700; line-height: 1.05;
  }
  .tagline .line-1 { color: var(--orange); font-size: 38px; display: block; }
  .tagline .line-2 { color: var(--charcoal); font-size: 46px; display: block; }
  .hero {
    height: 335px;
    background: linear-gradient(180deg, #8fb3d6 0%, #d8b47c 35%, #e6cf5a 60%, #d9b88a 100%);
  }
  .band { height: 16px; background: var(--orange); }
  .band.thin { height: 14px; }
  .gallery {
    height: 386px;
    background: linear-gradient(var(--gallery-top), var(--gallery-bottom));
    display: grid;
    grid-template-columns: 255px 217px 217px;
    grid-template-rows: 163px 163px;
    column-gap: 18px; row-gap: 18px;
    padding: 22px 0 0 54px;
  }
  .tile {
    border: 3px solid var(--frame);
    box-shadow: 0 6px 8px -4px rgba(0,0,0,.35);
  }
  .tile.tall { grid-row: 1 / span 2; background: linear-gradient(#4f86c9, #9aa3a8 55%, #bfb7a6); }
  .tile.concrete { background: linear-gradient(#c9c6c0, #9c9994); }
  .tile.paving { background: linear-gradient(#8ab2d8 0%, #6a6b6d 55%, #3e3f42); }
  .tile.rebar { background: linear-gradient(#7b7c80, #5b5d62); }
  .tile.crane { background: linear-gradient(#2f7fd9, #5b9de6 60%, #9fa3a8); }
  .details {
    height: 196px;
    display: flex;
    padding: 14px 0 0 46px;
  }
  .about { width: 478px; }
  .about h2 {
    color: var(--orange); font-size: 21px; font-weight: 700;
    line-height: 1; margin-bottom: 8px;
  }
  .about p {
    font-size: 12.2px; line-height: 16.5px; color: var(--ink);
    text-align: justify; font-weight: 600;
  }
  .cta { margin-left: 40px; padding-top: 14px; }
  .cta-title {
    font-family: "Oswald", "Arial Narrow", sans-serif;
    color: var(--orange); font-size: 56px; line-height: 1; font-weight: 700;
  }
  .cta-sub {
    color: var(--charcoal); font-weight: 700; font-size: 21px; line-height: 1.2;
  }
  .cta-phone {
    display: flex; align-items: center; gap: 10px; margin-top: 6px;
    font-weight: 700; font-size: 26px; color: var(--ink);
  }
  .cta-phone svg { width: 30px; height: 30px; }
  .contact-bar {
    height: 72px; display: flex; gap: 5px; margin-top: auto;
  }
  .contact-accent { width: 120px; background: var(--orange); }
  .contact-info {
    flex: 1; background: var(--charcoal);
    display: flex; align-items: center; gap: 24px; padding-left: 24px;
    color: #fff; font-size: 18.5px;
  }
  .contact-item { display: flex; align-items: center; gap: 10px; }
  .contact-item svg { width: 20px; height: 20px; }
</style>
</head>
<body>
  <main class="flyer">
    <div class="top-strip"></div>

    <header class="masthead">
      <div class="brand">
        <span class="brand-mark"></span>
        <span class="brand-name">Buildwise Hub</span>
      </div>
      <h1 class="tagline">
        <span class="line-1">Built by Construction</span>
        <span class="line-2">for Construction</span>
      </h1>
    </header>

    <div class="hero" role="img" aria-label="Photo of a roofer in a hard hat using a nail gun on timber roof trusses"></div>
    <div class="band"></div>

    <section class="gallery">
      <div class="tile tall" role="img" aria-label="Photo of high-rise towers under construction with tower cranes"></div>
      <div class="tile concrete" role="img" aria-label="Photo of workers pouring and spreading wet concrete"></div>
      <div class="tile paving" role="img" aria-label="Photo of a road paving crew with a roller and paver"></div>
      <div class="tile rebar" role="img" aria-label="Photo of a worker tying steel rebar mesh"></div>
      <div class="tile crane" role="img" aria-label="Photo of a concrete building frame and crane against blue sky"></div>
    </section>

    <div class="band thin"></div>

    <section class="details">
      <div class="about">
        <h2>ABOUT US</h2>
        <p>Lorem Ipsum is simply dummy text of the printing and pesetting industry.Lorem Ipsum has been the industry’s standard dummy text ever since the 1500s,when an unknown printer took a galley of type and scrambled it to make a type specimen book.Lorem Ipsum is simply dummy text of the printing and typesetting industry.Lorem Ipsum has been the industry’s standard dummy text ever since the 1500s,when an unknown printer took a galley of type and scrambled it to make a type specimen book.Lorem Ipsum is simply dummy text of the printing and typesetting industry.</p>
      </div>
      <div class="cta">
        <div class="cta-title">Register</div>
        <div class="cta-sub">your company now</div>
        <div class="cta-phone">
          <svg viewBox="0 0 24 24" aria-hidden="true"><path fill="#e0492a" d="M6.6 10.8c1.4 2.8 3.8 5.1 6.6 6.6l2.2-2.2c.3-.3.7-.4 1-.2 1.1.4 2.3.6 3.6.6.6 0 1 .4 1 1V20c0 .6-.4 1-1 1C10.6 21 3 13.4 3 4c0-.6.4-1 1-1h3.5c.6 0 1 .4 1 1 0 1.3.2 2.5.6 3.6.1.3 0 .7-.2 1l-2.3 2.2z"/></svg>
          <span>012-555-0147</span>
        </div>
      </div>
    </section>

    <footer class="contact-bar">
      <div class="contact-accent"></div>
      <div class="contact-info">
        <span class="contact-item">
          <svg viewBox="0 0 24 24" aria-hidden="true"><rect x="3" y="6" width="18" height="13" fill="none" stroke="#fff" stroke-width="1.6"/><path d="M3 6l9 7 9-7" fill="none" stroke="#fff" stroke-width="1.6"/></svg>
          info@buildwisehub.com
        </span>
        <span class="contact-item">
          <svg viewBox="0 0 24 24" aria-hidden="true"><rect x="3" y="4" width="18" height="12" fill="none" stroke="#fff" stroke-width="1.6"/><path d="M9 20h6M12 16v4" stroke="#fff" stroke-width="1.6"/></svg>
          www.buildwisehub.com
        </span>
      </div>
    </footer>
  </main>
</body>
</html>
```